New Billboard Design Project

I would like to have a banner made which is approx 16ft wide x 8ft tall showing our 3 businesses. I would like to use the new Ridgeline Depot Logo as the main , and have them all incorporated in one banner. I would like to have a nice background that would go with construction, excavation and material supply yard which sells landscape materials,
Updates

Adding photos to be incorporated

Target Market(s)

contractors, homeowners, landscapers, developers

Industry/Entity Type

Construction, land clearing, concrete foundations, Excaavation

Requirements
Must have
• excavation, concrete, all three logos

```html
<!DOCTYPE html>
<html lang="en">
<head>
<meta charset="utf-8">
<title>Ridgeline Depot Billboard</title>
<link href="https://fonts.googleapis.com/css2?family=Montserrat:ital,wght@0,600;0,700;0,800;1,600&display=swap" rel="stylesheet">
<style>
  :root {
    --maroon: #6b1f24;
    --green: #1f9a46;
    --ink-grey: #8a8a8a;
    --panel-top: #ffffff;
    --panel-bottom: #e4e4e6;
    --stage: #3f3c3e;
    --white: #ffffff;
  }
  * { margin: 0; padding: 0; box-sizing: border-box; }
  html, body {
    width: 1200px; height: 1200px; overflow: hidden;
    background: var(--stage);
    font-family: "Montserrat", sans-serif;
  }
  .billboard {
    position: absolute; left: 40px; top: 320px;
    width: 1120px; height: 560px;
    background: linear-gradient(180deg, var(--panel-top), var(--panel-bottom));
    overflow: hidden;
  }
  .billboard-shapes { position: absolute; inset: 0; }
  .brand {
    position: absolute; left: 26px; top: 34px;
    display: flex; align-items: center; gap: 14px;
  }
  .brand-mark { width: 22px; height: 22px; border-radius: 50%; background: var(--green); }
  .brand-name {
    color: var(--maroon); font-weight: 800; font-size: 44px;
    line-height: 0.98; letter-spacing: -0.5px; text-transform: uppercase;
  }
  .headline {
    position: absolute; left: 24px; top: 186px;
    font-weight: 700; text-transform: uppercase; letter-spacing: -1px;
  }
  .headline-line { display: block; color: var(--maroon); font-size: 51px; line-height: 50px; }
  .headline-accent { display: block; color: var(--green); font-size: 35px; line-height: 42px; letter-spacing: -1.2px; }
  .divider {
    position: absolute; left: 26px; top: 336px; width: 430px; height: 2px;
    background: var(--ink-grey);
  }
  .partners {
    position: absolute; left: 60px; top: 352px; width: 380px; height: 84px;
    display: flex; align-items: center;
  }
  .partner { flex: 1; text-align: center; color: var(--maroon); font-weight: 700; text-transform: uppercase; }
  .partner-name { font-size: 19px; line-height: 22px; }
  .partner-sub { font-size: 8.5px; letter-spacing: 1.5px; line-height: 14px; }
  .partner-sep { width: 2px; height: 80px; background: var(--maroon); opacity: .6; }
  .contact { position: absolute; left: 58px; top: 468px; color: var(--white); }
  .contact-cta { font-style: italic; font-weight: 600; font-size: 22px; line-height: 24px; }
  .contact-phone { font-weight: 700; font-size: 56px; line-height: 60px; letter-spacing: .5px; }
</style>
</head>
<body>
  <section class="billboard">
    <svg class="billboard-shapes" width="1120" height="560" viewBox="0 0 1120 560">
      <defs>
        <linearGradient id="site-photo" x1="0" y1="0" x2="0" y2="1">
          <stop offset="0" stop-color="#6f9ed1"/>
          <stop offset="0.35" stop-color="#d6dde6"/>
          <stop offset="0.6" stop-color="#d9b256"/>
          <stop offset="1" stop-color="#9c7c5a"/>
        </linearGradient>
      </defs>
      <path class="maroon-sweep" fill="var(--maroon)"
            d="M586,0 C470,120 468,310 618,462 L0,462 L0,560 L1120,560 L1120,0 Z"/>
      <path class="site-photo" fill="url(#site-photo)" role="img"
            aria-label="Photo of two yellow excavators on a dirt mound under a cloudy blue sky"
            d="M638,0 C520,140 540,380 721,560 L1120,560 L1120,0 Z"/>
    </svg>

    <div class="brand">
      <span class="brand-mark"></span>
      <div class="brand-name">Ridgeline<br>Depot</div>
    </div>

    <h1 class="headline">
      <span class="headline-line">Construction</span>
      <span class="headline-line">Excavation &amp;</span>
      <span class="headline-accent">Material Supply Yard</span>
    </h1>

    <div class="divider"></div>

    <div class="partners">
      <div class="partner">
        <div class="partner-name">Kestrel</div>
        <div class="partner-sub">Excavation Co.</div>
      </div>
      <div class="partner-sep"></div>
      <div class="partner">
        <div class="partner-name">Birchwood Homes</div>
        <div class="partner-sub">Construction Co.</div>
      </div>
    </div>

    <div class="contact">
      <div class="contact-cta">CALL US TODAY</div>
      <div class="contact-phone">555.010.2400</div>
    </div>
  </section>
</body>
</html>
```